Quelvo service sheets and folder

A set of 12 Service sheets plus a rate card to be inserted into a folder - each to be designed and formatted.
A4
Portrait
- the idea is to keep things simple and crisp.
I would use the logo (see attached .ai file) at the top and maybe an separate image to go with each sheet

Around 350 words per page (see attached example)
The format is mainly text and bullet points, but each page will be same layout (just a different image as indicated above).

Need to factor in a folder to hold the service sheets.

The documents to have a good sales impact and your experience and advice on best ideas would be welcome. The key is to keep it crisp, elegant & professional for financial services.

The output files should be in PDF and raw file formats so that printing can be managed easily in future., Details for my new Catalogue Design Project will be added soon.

Industry/Entity Type

Financial

Requirements
Must have
• Inspire us!
Should not have
• No images of people or parts (like hands, arms) etc

```html
<!DOCTYPE html>
<html lang="en">
<head>
<meta charset="utf-8">
<title>Quelvo – Investment Management Services</title>
<link href="https://fonts.googleapis.com/css2?family=Jost:wght@300;400&display=swap" rel="stylesheet">
<style>
  :root {
    --paper: #ffffff;
    --ink: #2b2b2b;
    --ink-soft: #3a3a3a;
    --band: #1e1e1e;
    --accent-green: #6fb33f;
    --accent-red: #d9262a;
    --brand-purple: #5b2a86;
    --photo-light: #eef3f8;
    --photo-mid: #bcd3ea;
    --photo-deep: #3f7fc6;
  }
  * { margin: 0; padding: 0; box-sizing: border-box; }
  html, body {
    width: 898px;
    height: 1200px;
    overflow: hidden;
    background: var(--paper);
  }
  .sheet {
    position: relative;
    width: 898px;
    height: 1200px;
    background: var(--paper);
    font-family: "Jost", "Futura", sans-serif;
    font-weight: 300;
    color: var(--ink);
  }
  .brand {
    position: absolute;
    top: 86px;
    right: 48px;
    display: flex;
    align-items: center;
    gap: 12px;
  }
  .brand-mark {
    width: 22px;
    height: 22px;
    border-radius: 50%;
    background: var(--brand-purple);
  }
  .brand-name {
    font-size: 30px;
    font-weight: 400;
    letter-spacing: 1px;
    color: var(--ink);
  }
  .sheet-title {
    position: absolute;
    top: 154px;
    left: 0;
    width: 100%;
    text-align: center;
    font-size: 42px;
    font-weight: 300;
    color: var(--ink);
  }
  .hero-image {
    position: absolute;
    top: 233px;
    left: 75px;
    width: 757px;
    height: 296px;
    background: linear-gradient(160deg, var(--photo-mid) 0%, var(--photo-light) 45%, #ffffff 60%, var(--photo-mid) 85%, var(--photo-deep) 100%);
  }
  .content {
    position: absolute;
    top: 554px;
    left: 122px;
    width: 710px;
    font-size: 19px;
    line-height: 28px;
    color: var(--ink-soft);
  }
  .content p {
    text-align: justify;
    text-indent: 30px;
    margin-bottom: 18px;
    hyphens: auto;
  }
  .content .tagline {
    text-align: left;
    margin-bottom: 18px;
  }
  .contact {
    position: absolute;
    left: 41px;
    top: 1088px;
    font-size: 19px;
    color: var(--ink-soft);
  }
  .contact-row {
    display: flex;
    align-items: center;
    gap: 10px;
    margin-top: 12px;
  }
  .contact-row svg { display: block; }
  .contact-gap { width: 22px; }
  .footer-band {
    position: absolute;
    left: 0;
    bottom: 0;
    width: 898px;
    height: 70px;
  }
  .web-address {
    position: absolute;
    right: 50px;
    bottom: 32px;
    font-size: 26px;
    letter-spacing: 4px;
    color: #ffffff;
    font-weight: 400;
  }
</style>
</head>
<body>
<main class="sheet">
  <header class="brand">
    <span class="brand-mark"></span>
    <span class="brand-name">QUELVO</span>
  </header>

  <h1 class="sheet-title">Investment Management Services</h1>

  <div class="hero-image" role="img" aria-label="Photograph of advisers reviewing printed financial charts and graphs on a desk"></div>

  <section class="content">
    <p class="tagline">Simplifying investing; with your portfolio managed by professionals</p>
    <p>A bespoke service tailored to your needs, with a dedicated investment manager taking over the burden of monitoring and managing your portfolio of investments.</p>
    <p>The Discretionary Investment Management Service passes the burden of managing your portfolio of investments to a dedicated investment manager. Investments are targeted to provide the best returns matched to your stated risk profile and investment objectives. Your investment manager is available to discuss any aspect of your investments and you will be regularly updated with the performance of your portfolio.</p>
  </section>

  <footer>
    <address class="contact" style="font-style: normal;">
      <div>12 Marlow Court, London, EC2R 7HN</div>
      <div class="contact-row">
        <svg width="22" height="22" viewBox="0 0 22 22" aria-hidden="true">
          <circle cx="11" cy="11" r="9.5" fill="none" stroke="var(--accent-red)" stroke-width="1.6"/>
          <path d="M8 6.5c-1 .6-1.4 1.6-1 3 .6 2.2 2.3 4.3 4.4 5.4 1.2.6 2.3.5 3-.4l-1.6-1.6-1.2.7c-1-.6-1.9-1.6-2.4-2.7l.9-1-1.2-2.1z" fill="var(--accent-red)"/>
        </svg>
        <span>+44 (0) 20 7946 0321</span>
        <span class="contact-gap"></span>
        <svg width="22" height="18" viewBox="0 0 22 18" aria-hidden="true">
          <rect x="1" y="2" width="20" height="14" rx="2" fill="var(--accent-red)"/>
          <path d="M3 4.5l8 6 8-6" fill="none" stroke="#ffffff" stroke-width="1.6"/>
        </svg>
        <span>info@quelvo.com</span>
      </div>
    </address>

    <svg class="footer-band" width="898" height="70" viewBox="0 0 898 70" aria-hidden="true">
      <rect x="0" y="36" width="898" height="7" fill="var(--accent-green)"/>
      <rect x="0" y="43" width="898" height="27" fill="var(--band)"/>
      <path d="M530 43 C560 43 565 0 610 0 L898 0 L898 70 L530 70 Z" fill="var(--band)"/>
    </svg>
    <div class="web-address">www.quelvo.com</div>
  </footer>
</main>
</body>
</html>
```